new roofing company card

New primary business card for roofing company.

Industry/Entity Type

Residential roofing/Specializing in Asphalt and Standing seam metal roofing

Contact Information for Business Card

Phone number is: 484 672 1058 Email: support@fennridgeroofworks.com website: www.fennridgeroofworks.com

Colors
EB3D1F
EC4F4E
F09395
F8D3D4
FCEDEE

```html
<!DOCTYPE html>
<html lang="en">
<head>
<meta charset="utf-8">
<title>Fennridge Roofworks Business Card</title>
<link rel="stylesheet" href="https://fonts.googleapis.com/css2?family=Cinzel:wght@500;700&family=Montserrat:wght@400;500&display=swap">
<style>
  :root {
    --bg: #e4e2e3;
    --ink: #232323;
    --ink-deep: #161616;
    --white: #ffffff;
    --red: #c8332a;
    --red-bright: #eb3d1f;
    --pattern-hi: #4a4a4a;
  }
  * { box-sizing: border-box; margin: 0; padding: 0; }
  html, body { width: 1200px; height: 912px; overflow: hidden; }
  body {
    background: var(--bg);
    display: flex;
    flex-direction: column;
    align-items: center;
    justify-content: center;
    gap: 40px;
    font-family: "Montserrat", sans-serif;
  }
  .card {
    position: relative;
    width: 560px;
    height: 320px;
    border-radius: 16px;
    overflow: hidden;
    box-shadow: 0 10px 26px rgba(0,0,0,0.22);
  }
  /* Back */
  .card-back { background: var(--ink-deep); }
  .card-back .pattern-field {
    position: absolute; inset: 0;
    background: linear-gradient(120deg, #141414 0%, #1d1d1d 45%, var(--pattern-hi) 62%, #242424 70%, #2e2e2e 100%);
  }
  .card-back .back-mark {
    position: absolute;
    right: 34px; bottom: 30px;
    font-family: "Cinzel", serif;
    font-weight: 700;
    font-size: 15px;
    letter-spacing: 1px;
    color: var(--red);
  }
  /* Front */
  .card-front { background: var(--white); }
  .card-front .wave { position: absolute; inset: 0; width: 100%; height: 100%; }
  .brand {
    position: absolute;
    left: 38px; top: 112px;
    width: 230px;
    text-align: center;
    font-family: "Cinzel", serif;
    font-weight: 700;
    color: var(--ink);
    line-height: 1.05;
  }
  .brand .brand-main { display: block; font-size: 31px; }
  .brand .brand-sub { display: block; font-size: 19px; letter-spacing: 3px; margin-top: 4px; }
  .contact {
    position: absolute;
    right: 26px; top: 158px;
    text-align: right;
    color: var(--white);
  }
  .contact .person {
    font-family: "Cinzel", serif;
    font-weight: 500;
    font-size: 21px;
    color: var(--red);
    letter-spacing: 0.5px;
  }
  .contact .role { font-size: 11px; margin-top: 1px; margin-right: 20px; }
  .contact .lines { list-style: none; margin-top: 12px; }
  .contact .lines li {
    font-size: 11.5px;
    display: flex;
    justify-content: flex-end;
    align-items: center;
    gap: 7px;
    margin-bottom: 7px;
  }
  .contact .icon { width: 11px; height: 11px; flex: none; }
</style>
</head>
<body>

<section class="card card-back">
  <div class="pattern-field" role="img" aria-label="Glossy black surface covered in a repeating tonal monogram pattern"></div>
  <span class="back-mark">FENNRIDGE</span>
</section>

<section class="card card-front">
  <svg class="wave" viewBox="0 0 560 320" preserveAspectRatio="none" aria-hidden="true">
    <path d="M0 286 C120 262 250 262 330 170 C390 95 420 40 470 22 C500 12 530 8 560 6 L560 320 L0 320 Z" fill="var(--ink)"/>
    <path d="M0 276 C120 252 245 252 322 164 C382 90 412 30 462 14 C494 4 528 0 556 -2" fill="none" stroke="var(--red)" stroke-width="6"/>
    <path d="M40 283 C150 262 250 260 316 188 C350 150 370 110 392 80" fill="none" stroke="var(--red)" stroke-width="1.5"/>
  </svg>

  <div class="brand">
    <span class="brand-main">FENNRIDGE</span>
    <span class="brand-sub">ROOFWORKS</span>
  </div>

  <div class="contact">
    <p class="person">DALEN MARSH</p>
    <p class="role">Managing Director</p>
    <ul class="lines">
      <li>484 672 1058
        <svg class="icon" viewBox="0 0 12 12" aria-hidden="true"><path d="M3 1 L5 3.5 L4 5 C4.8 6.6 5.6 7.4 7 8 L8.5 7 L11 9 L9.6 11 C5 10.6 1.4 7 1 2.4 Z" fill="var(--red)"/></svg>
      </li>
      <li>support@fennridgeroofworks.com
        <svg class="icon" viewBox="0 0 12 12" aria-hidden="true"><rect x="1" y="2.5" width="10" height="7" fill="var(--red)"/><path d="M1 2.5 L6 6.5 L11 2.5" fill="none" stroke="var(--ink)" stroke-width="1"/></svg>
      </li>
      <li>www.fennridgeroofworks.com
        <svg class="icon" viewBox="0 0 12 12" aria-hidden="true"><circle cx="6" cy="6" r="5" fill="none" stroke="var(--red)" stroke-width="1.2"/><ellipse cx="6" cy="6" rx="2.2" ry="5" fill="none" stroke="var(--red)" stroke-width="1"/><path d="M1 6 H11" stroke="var(--red)" stroke-width="1"/></svg>
      </li>
    </ul>
  </div>
</section>

</body>
</html>
```